Kleine Website f. Unternehmensdarstellung
Zielgruppe
Geschäftsführer, Marketing & Sales Manager asiatischer Konzerne.
Aufgabenstellung
Wir sind eine Consulting und Handelsagentur mit überwiegend internationaler Kundschaft (Asien 70%).
Für einen Webauftritt, ca. 8 Seiten, haben wir eine Powerpoint Vorlage erstellt, diese zeigt nur die Inhalte. Wir benötigen nun daraus eine Website, haben eigenen Webspace, eigener Server bei Hostquelle. Wir stellen uns als Hintergrundbild auf der Frontpage Hongkong vor. Keine Flash videos oder audio einbindung ! Sprache Englisch, die Texte sollten von uns leicht editierbar sein, falls mal Anpassungen gemacht werden müssen.

```html
<!DOCTYPE html>
<html lang="en">
<head>
<meta charset="utf-8">
<title>Corvane Group – Trouble Shooting</title>
<link rel="stylesheet" href="https://fonts.googleapis.com/css2?family=Noto+Sans:wght@400;700&display=swap">
<style>
  :root {
    --night: #0c0c0d;
    --sky: #1a1c22;
    --glow-warm: #6b5230;
    --glow-cool: #3d4a5c;
    --panel: rgba(214, 214, 216, 0.86);
    --ink: #1b1b1b;
    --white: #f4f4f4;
    --muted: #8a8a8a;
  }
  * { box-sizing: border-box; margin: 0; padding: 0; }
  html, body { width: 1200px; height: 788px; overflow: hidden; background: var(--night); }
  body { font-family: "Noto Sans", sans-serif; color: var(--ink); position: relative; }

  .skyline-photo {
    position: absolute; inset: 0;
    background:
      radial-gradient(ellipse 260px 200px at 130px 470px, rgba(107, 82, 48, 0.55), transparent 70%),
      radial-gradient(ellipse 260px 220px at 1100px 480px, rgba(107, 82, 48, 0.5), transparent 70%),
      radial-gradient(ellipse 180px 420px at 900px 300px, rgba(61, 74, 92, 0.6), transparent 75%),
      linear-gradient(180deg, var(--night) 0%, var(--sky) 30%, #2a2622 62%, #151413 78%, var(--night) 86%);
  }

  .site-header { position: absolute; top: 0; left: 198px; width: 804px; height: 60px; }
  .welcome { position: absolute; left: 0; top: 19px; font-size: 18px; color: var(--white); letter-spacing: -0.2px; }
  .brand {
    position: absolute; right: 0; top: 12px;
    display: flex; align-items: center; gap: 10px;
    font-size: 29px; font-weight: 700; color: var(--white); letter-spacing: 3px;
  }
  .brand-mark { width: 22px; height: 22px; background: var(--white); }

  .intro {
    position: absolute; top: 76px; left: 0; width: 1200px; padding-left: 66px;
    text-align: center; font-size: 17px; color: var(--white);
  }

  .content-panel {
    position: absolute; left: 198px; top: 120px; width: 804px; height: 568px;
    background: var(--panel); border-radius: 5px;
    padding: 28px 28px 0 32px;
  }
  .content-panel h1 { font-size: 20px; font-weight: 700; margin-bottom: 12px; letter-spacing: 0.1px; }
  .content-panel h2 { font-size: 14px; font-weight: 700; margin-bottom: 10px; padding-left: 1px; }
  .content-panel p { font-size: 13.6px; line-height: 17.2px; margin-bottom: 15.5px; letter-spacing: 0.05px; }
  .content-panel p.closing { margin-top: 22px; padding-right: 20px; }

  .site-footer { position: absolute; top: 699px; left: 0; width: 1200px; text-align: center; }
  .footer-nav { display: flex; justify-content: center; gap: 30px; padding-left: 10px; }
  .footer-nav a { font-size: 9.5px; color: var(--muted); text-decoration: none; }
  .copyright { margin-top: 8px; font-size: 9.5px; color: var(--muted); padding-left: 2px; }
</style>
</head>
<body>
  <div class="skyline-photo" role="img" aria-label="Night photograph of the Hong Kong skyline with illuminated towers and harbour lights"></div>

  <header class="site-header">
    <div class="welcome">Welcome to the Corvane Group...</div>
    <div class="brand"><span class="brand-mark"></span>CORVANE</div>
  </header>

  <p class="intro">Our business segments cover quite an area, please select your piont of interest :</p>

  <main class="content-panel">
    <h1>Trouble Shooting</h1>
    <h2>Here are proven real world testimonies:</h2>
    <p>A helicopter manufacturer had ordered laser warning sensors. The laser warning sensor supplier had a working prototype. 300 helicopters have been ordered by mother- but the laser warner never worked out, just the prototype, that´s all. Multi million dollars value stuck in the production chain of the chopper manufacturer.</p>
    <p>Within six month we developed a new sensor from scratch, got the pricing down 30%, got an AQAP production line up and testified and, finally, got reliable sensors ! Saved millions of $ penalties, earned millions of $ sales.</p>
    <p>A huge global player needed an optical sensor for a multi million $ laser drilling machine, capable in aiming a banknote on the moon. Again, prototypes worked, but never ever an industrial manufacturing and QC system. We fixed it within only four months.</p>
    <p>One customer designed in a complicated part from a foreign country vendor. The foreign country changed the export rules, even simple parts dropped under a „governmental regulation“. Aircrafts were globally grounded, huge computer cores were in danger. We got a qualified second source within 8 weeks.</p>
    <p>An automotive company, together with their „preferred vendor“, designed a nice steering wheel sensor. All was done, designed in, the preferred vendor“ went bankrupt, the production line of the automotive company just went online. Great .... We needed eight weeks ...</p>
    <p>Some military (small)talk, „friendly fire“ is the name of the monster. All is infrared, nothing was coded, everything was killed.We did emitters and sensors, capeable in differentiating friend or foe...</p>
    <p class="closing">We do all these jobs on a high security level as well on a high personal confidence level - means, nobody will be blamed. Never. We are the buddies everyone can beat on and casts stones from heaven, if it is not going to work out ...so far, in all humbleness, we have never left this policy. Nor we will .... And we have been battered in only ONE case, but this we explain to you face to face ...</p>
  </main>

  <footer class="site-footer">
    <nav class="footer-nav">
      <a href="#">Home</a>
      <a href="#">Agency</a>
      <a href="#">Consultancy</a>
      <a href="#">Technology Finance</a>
      <a href="#">Troubleshooting</a>
      <a href="#">M&amp;A Silent Service</a>
    </nav>
    <p class="copyright">Copyright 2010. Corvane Group. All Rights Reserved.</p>
  </footer>
</body>
</html>
```